Artist needs a Wordpress Website design to market my original paintings

Mona Breckell Gallery.com
Artist - Original Abstract Paintings

Artist needs classy and elegant WORDPRESS website to market my Original Paintings.
What sets these paintings apart?
Each one was inspired by the inner connection between the artist and the individual destined to receive the painting. Paintings are priced high end and require a website to reflect their high quality.
Website must be responsive on all devices. eg. mobile, laptop and desktop. It must have a shopping cart in order to complete sales.
The domain name monabreckellgallery.com has already been purchased and is hosted on Servanta.
I want it to be very easy to navigate and also easy for me to add and edit more images and content.
I have no official logo but you can insert the title,
Mona Breckell
Collection
Original Fluid Art Paintings
in whatever design/font format you feel attractive, I leave that to the designer. I want it to be simple and include a lot of negative space to avoid a cluttered look. The paintings are colorful on their own and prefer not to detract from them as a focal point. I leave the color theme to the designer. Perhaps you may like to extract a color theme from one of the paintings.
Requirements:
5 pages: HOME, ABOUT, SHOP, CART, CONTACT
Home page:
-Menu across the top
-1 large painting (prefer the purple and green painting)
-3 smaller images below the large one
Unless you come up with a more professional format.
ABOUT:
(You can include my uploaded photo for now on the ABOUT page. I will replace it when I get a professional photo.)
I learned I am never too old to re-invent my life. Lesson learned. At the age of 78 and after the ending of my 30 years of marriage I was faced with an unexpected change in my life circumstances. I made the decision to re-invent my life.
Art, in varying media has always been a part of my experience as a hobby. When I was presented with fluid art, my life as I had known it turned to excitement, and discovery, carving a promising vision of my future.
My spiritual training has taught me how to recognize my connection with people inwardly. With this awareness it became clear to me while painting that I was creating a work of art for a specific individual. I allow creative expression to flow through me that is destined for you. I do not know who you are, but if you recognize the painting that inspires you, I have succeeded with our connection.
I live in Washington State, USA
I am looking forward to meeting you.
Mona Breckell
SHOP:
This should be the gallery from which one can shop. The images will be more like a thumbprint but large enough to see well, perhaps 3 across the page. As one hovers over, or clicks on one, it will link to a page with a larger view that has:
-Description
-Price and a CHOICE to click on
-Add to Cart Button OR
-Continue shopping (so they don't have to go back to homepage)
This page should be a scrolling one so eventually all of my paintings will be added to this page and easy for someone to shop instead of going back and forth between pages.
Please set this up (making it a link to larger image, etc) and include one or all of the images I upload here. I will add the rest.

CART:
-Add a shopping cart

CONTACT:
-email: breckellgallery@mailorbit.net
All pages should have a link back to the homepage.
SOCIAL MEDIA LINKS:
-Snapvista:
http://snapvista.net/monabreckellgallery
-Friendloop
https://www.friendloop.net/ourchosenworks/?
view_public_for=407385291164273

http://corinnalubeckstudio.net
eg of a website that I like the navigation. I like the simplicity of the Home Page but the photo is too large. A smaller main photo and 3 smaller ones beneath it would have looked nicer to me.

```html
<!DOCTYPE html>
<html lang="en">
<head>
<meta charset="utf-8">
<title>Mona Breckell Collection – Original Paintings</title>
<link href="https://fonts.googleapis.com/css2?family=Great+Vibes&family=Lato:wght@400;700&display=swap" rel="stylesheet">
<style>
:root{
  --plum:#652a58;
  --mint:#3fcf8e;
  --ink:#1c1c1c;
  --body:#5a5a5a;
  --white:#ffffff;
}
*{margin:0;padding:0;box-sizing:border-box}
html,body{width:1059px;height:1200px;overflow:hidden;background:var(--white);font-family:"Lato",sans-serif}
.page{position:relative;width:1059px;height:1200px}

.site-header{position:absolute;top:0;left:0;width:100%;height:68px;background:var(--white)}
.brand{position:absolute;left:97px;top:20px;font-family:"Lato",sans-serif;font-weight:400;font-size:22px;color:var(--ink);line-height:28px;letter-spacing:.3px}
.main-nav{position:absolute;left:439px;top:25px;display:flex;gap:27px;font-size:13px;font-weight:700;letter-spacing:.1px}
.main-nav a{color:var(--ink);text-decoration:none;padding-bottom:3px}
.main-nav a.is-active{color:var(--mint);border-bottom:2px solid var(--mint)}
.cart{position:absolute;left:751px;top:16px;width:36px;height:36px;border:2px solid var(--plum);border-radius:50%}
.cart svg{position:absolute;left:8px;top:9px}
.cart-count{position:absolute;left:24px;top:-7px;width:17px;height:17px;border-radius:50%;background:var(--mint);color:var(--white);font-size:11px;font-weight:700;text-align:center;line-height:17px}
.btn{display:inline-flex;align-items:center;justify-content:center;gap:9px;background:var(--plum);color:var(--white);font-weight:700;text-decoration:none;border-radius:28px}
.btn-subscribe{position:absolute;left:837px;top:14px;width:124px;height:40px;font-size:13px}

.hero{position:absolute;top:68px;left:0;width:1059px;height:513px;
  background:
   radial-gradient(ellipse 260px 200px at 560px 110px,#3ee07a 0%,rgba(62,224,122,0) 100%),
   radial-gradient(ellipse 300px 260px at 300px 380px,#9a5c9c 0%,rgba(154,92,156,0) 100%),
   radial-gradient(ellipse 220px 200px at 900px 180px,#6b3f72 0%,rgba(107,63,114,0) 100%),
   radial-gradient(ellipse 180px 240px at 40px 300px,#1c2326 0%,rgba(28,35,38,0) 100%),
   linear-gradient(135deg,#5a8a4a 0%,#7b4a80 40%,#3fcf7a 70%,#4a3a55 100%)}
.hero-title{position:absolute;left:0;top:0;width:100%;height:100%;text-align:center;font-family:"Great Vibes",cursive;color:var(--white);font-weight:400;line-height:1}
.hero-title .line-1{position:absolute;left:0;width:100%;top:150px;font-size:84px}
.hero-title .line-2{position:absolute;left:0;width:100%;top:250px;font-size:84px}

.intro{position:absolute;top:636px;left:130px;width:800px;text-align:center;color:var(--body);font-size:14.5px;line-height:26px}
.btn-search{position:absolute;left:441px;top:714px;width:179px;height:42px;font-size:13px}

.gallery{position:absolute;top:828px;left:98px;display:flex;gap:8px}
.tile{width:282px;height:211px}
.tile-1{background:radial-gradient(circle at 45% 50%,#f1e6ef 0%,#7c3a74 30%,#c08a3a 65%,#7a2a4a 100%)}
.tile-2{background:radial-gradient(circle at 60% 55%,#e8c9b4 0%,#9b3b3e 40%,#6a2a2e 75%,#c24a3a 100%)}
.tile-3{background:linear-gradient(120deg,#b76a2a 0%,#e9dccb 45%,#c25a24 70%,#efe3d6 100%)}

.site-footer{position:absolute;top:1124px;left:0;width:1059px;height:76px;background:var(--plum);color:var(--white)}
.footer-mail{position:absolute;left:99px;top:21px;display:flex;align-items:center;gap:19px;font-size:13px}
.icon-ring{width:34px;height:34px;border:1.5px solid var(--white);border-radius:50%;display:flex;align-items:center;justify-content:center}
.social{position:absolute;left:470px;top:29px;display:flex;gap:14px;font-size:13px;font-weight:400}
.social a{color:var(--white);text-decoration:none}
.copyright{position:absolute;right:98px;top:30px;font-size:13px}
</style>
</head>
<body>
<div class="page">
  <header class="site-header">
    <div class="brand">Original Paintings</div>
    <nav class="main-nav">
      <a href="#" class="is-active">HOME</a>
      <a href="#">ABOUT</a>
      <a href="#">CONTACT</a>
      <a href="#">SHOP</a>
    </nav>
    <div class="cart" aria-label="Cart">
      <svg width="17" height="14" viewBox="0 0 17 14"><path d="M0 1h3l2 8h9l2-6H4.5" fill="none" stroke="#3fcf8e" stroke-width="2"/><circle cx="6" cy="12" r="1.5" fill="#3fcf8e"/><circle cx="13" cy="12" r="1.5" fill="#3fcf8e"/></svg>
      <span class="cart-count">0</span>
    </div>
    <a href="#" class="btn btn-subscribe">SUBSCRIBE
      <svg width="12" height="12" viewBox="0 0 12 12"><circle cx="6" cy="6" r="6" fill="#fff"/><path d="M5 3.5 7.5 6 5 8.5" fill="none" stroke="#652a58" stroke-width="1.8"/></svg>
    </a>
  </header>

  <section class="hero" role="img" aria-label="Featured purple and green fluid art painting">
    <h1 class="hero-title"><span class="line-1">Mona Breckell</span><span class="line-2">Collection</span></h1>
  </section>

  <p class="intro">I allow creative expression to flow through me that is destined specifically for you. I do not know who you are,<br>but if you recognize the painting that inspires you, I have succeeded with our connection.</p>
  <a href="#" class="btn btn-search">SEARCH for YOURS
    <svg width="12" height="12" viewBox="0 0 12 12"><circle cx="6" cy="6" r="6" fill="#fff"/><path d="M5 3.5 7.5 6 5 8.5" fill="none" stroke="#652a58" stroke-width="1.8"/></svg>
  </a>

  <section class="gallery">
    <div class="tile tile-1" role="img" aria-label="Fluid art painting with a white and purple burst on gold"></div>
    <div class="tile tile-2" role="img" aria-label="Fluid art painting with pale floral swirls on deep red"></div>
    <div class="tile tile-3" role="img" aria-label="Fluid art painting in copper orange and cream cells"></div>
  </section>

  <footer class="site-footer">
    <div class="footer-mail">
      <span class="icon-ring"><svg width="16" height="12" viewBox="0 0 16 12"><rect x="1" y="1" width="14" height="10" rx="2" fill="none" stroke="#fff" stroke-width="1.5"/><path d="M1.5 2 8 7l6.5-5" fill="none" stroke="#fff" stroke-width="1.5"/></svg></span>
      <span>breckellgallery@mailorbit.net</span>
    </div>
    <div class="social">
      <a href="#">Friendloop</a>
      <a href="#">Snapvista</a>
    </div>
    <div class="copyright">© 2020 Mona Breckell. All Rights Reserved</div>
  </footer>
</div>
</body>
</html>
```